Corporate services company needs a brochure

We are starting a company offering setup services to companies new to that location.
This includes services such as recruitment, company formation, advertising, marketing, pr, handling legal issues, logistics, transportation, procurement,immigration services, corporate gifts, accomodation,entertainment, training, administrative services etc.
Basically taking the setup issues off the hands of the company allowing them focus on their core business.

We are looking to design a professional brochure which would give the potential customers the confidence to entrust us with their needs.

We will be including some copy that can be used but i would very much like for you to bring what i have written to life - adding, deducting and amending where required.

We are looking at a A4 4/6 paged brochure but open to suggestions.

                                       

If you have any images that are suitable, please let us know. We will also be searching for some to add.

The first prize has been increased.

Thanks

Reason: We have just guaranteed the payment and we are hoping that this will encourage good designers to participate.

Reason: Some designers have requested more time to complete their final design.

Hi, I h extended the deadline to give designers more time to work on designs.

we are also looking at making the brochure a height of 8.5 and a width of 11. Please let me know your thoughts on this as any advice will help. The whole objective is to make it look as up to date and creative as possible. There is also another design size of 7.5 by 8.5

Thanks

                                        Hi

The copy has been revised and uploaded.

Hopefully it will give a clearer explanation of what we are trying to do.

Please let me know if you have any further questions.

Thanks

Mabel

Reason: adding finishing touches to designs

Reason: We are amending the copy for the brochure

Reason: The new copy for the brochure is ready. I am sorry it has taken so long to get it out. I am sure we will not be making any amendments to it post today. Thanks for your patience The extension is not to attact new designs it is for existing designs's copy to be modified to include information from the updated copy.

medium to large companies in banking, telecom, retail etc. It will be viewed by middle and top management.

Legal

• The brochure must clearly highlight all our services without just listing as this would risk it appearing as if we have just included everything we could think of!,
Please do not do the sitting round the conference table brochure or the typical blue and white brochure.
I desperately need it to be different, unique and serious enough to show that we are capable of handling/managing all what we have included.
Our clients include the many companies starting up an office in Africa.
We are anxious to have the potential clients understand that we will help them setup under any climax/
• modern colours but not too bright. there must still be a clear serious edge to it.
• conference room table and people sitting around it.
the typical blue and white brochures often used for these type of services.

```html
<!DOCTYPE html>
<html lang="en">
<head>
<meta charset="utf-8">
<title>Corvane Universal Services Limited — Brochure Cover Spread</title>
<link rel="stylesheet" href="https://fonts.googleapis.com/css2?family=Special+Elite&family=Carlito:wght@400;700&display=swap">
<style>
  :root {
    --brand-orange: #f28321;
    --band-white: #ffffff;
    --ink-black: #0d0d0d;
    --ink-dark: #2b2b2b;
    --paper-white: #ffffff;
    --mark-grey: #4a4a4a;
  }
  * { margin: 0; padding: 0; box-sizing: border-box; }
  html, body {
    width: 1200px;
    height: 464px;
    overflow: hidden;
    background: var(--brand-orange);
  }
  .spread {
    position: relative;
    width: 1200px;
    height: 464px;
    background: var(--brand-orange);
    overflow: hidden;
  }

  /* Highlighted statement blocks */
  .statement {
    position: absolute;
    text-align: center;
    font-family: "Special Elite", "Courier New", monospace;
    font-variant: small-caps;
    font-size: 12px;
    letter-spacing: 2px;
    line-height: 19px;
    color: var(--paper-white);
    -webkit-text-stroke: 0.35px var(--paper-white);
  }
  .statement__line { display: block; }
  .statement__line span {
    background: var(--ink-black);
    padding: 2px 7px 3px;
    white-space: nowrap;
  }
  .statement--intro   { left: 25px;  top: 38px;  width: 430px; }
  .statement--startup { left: 181px; top: 329px; width: 430px; }
  .statement--support { left: 817px; top: 342px; width: 380px; }

  /* Central white band */
  .info-band {
    position: absolute;
    left: 0;
    top: 181px;
    width: 1200px;
    height: 57px;
    background: var(--band-white);
  }
  .info-band__company {
    position: absolute;
    left: 48px;
    top: 21px;
    font-family: "Special Elite", "Courier New", monospace;
    font-variant: small-caps;
    font-size: 12px;
    letter-spacing: 2px;
    color: var(--ink-dark);
  }
  .info-band__address {
    position: absolute;
    left: 318px;
    top: 23px;
    font-family: "Carlito", "Calibri", sans-serif;
    font-size: 11px;
    color: var(--ink-dark);
  }
  .brand-name {
    position: absolute;
    left: 632px;
    top: 19px;
    display: flex;
    align-items: center;
    gap: 6px;
    font-family: "Carlito", "Calibri", sans-serif;
    font-weight: 700;
    font-size: 14px;
    letter-spacing: 0.5px;
    color: var(--mark-grey);
  }
  .brand-name__square {
    width: 9px;
    height: 9px;
    background: var(--mark-grey);
  }
  .info-band__tagline {
    position: absolute;
    left: 769px;
    top: 20px;
    font-family: "Carlito", "Calibri", sans-serif;
    font-size: 16.5px;
    color: var(--brand-orange);
  }

  /* Cover title */
  .cover-title {
    position: absolute;
    right: 48px;
    top: 262px;
    text-align: right;
  }
  .cover-title__name {
    font-family: "Special Elite", "Courier New", monospace;
    font-variant: small-caps;
    font-weight: 400;
    font-size: 25px;
    letter-spacing: 3.4px;
    color: var(--paper-white);
    -webkit-text-stroke: 0.6px var(--paper-white);
    line-height: 28px;
  }
  .cover-title__slogan {
    font-family: "Carlito", "Calibri", sans-serif;
    font-size: 10px;
    color: var(--ink-black);
    line-height: 11px;
  }
</style>
</head>
<body>
<main class="spread">

  <section class="statement statement--intro">
    <p class="statement__line"><span>Today’s business environment is fast moving,</span></p>
    <p class="statement__line"><span>multi-faceted and highly competitive.</span></p>
    <p class="statement__line"><span>Business owners need the support of professionals</span></p>
    <p class="statement__line"><span>who provide on-time, efficient solutions</span></p>
    <p class="statement__line"><span>to help their business move forward.</span></p>
    <p class="statement__line"><span>We aim to provide such a service.</span></p>
  </section>

  <header class="info-band">
    <p class="info-band__company">Corvane Universal Services Limited</p>
    <p class="info-band__address">Palmgrove Terrace, Marina Point, Lagos Nigeria</p>
    <div class="brand-name"><span class="brand-name__square"></span>CORVANE</div>
    <p class="info-band__tagline">Providing business operation solutions for your company</p>
  </header>

  <div class="cover-title">
    <h1 class="cover-title__name">Corvane Universal Services Limited</h1>
    <p class="cover-title__slogan">Service beyond the surface</p>
  </div>

  <section class="statement statement--startup">
    <p class="statement__line"><span>We are a ‘one-stop’ shop for startups</span></p>
    <p class="statement__line"><span>– whether you’re still in pitch-deck modes</span></p>
    <p class="statement__line"><span>or further along in the process of</span></p>
    <p class="statement__line"><span>starting your new venture in Nigeria,</span></p>
    <p class="statement__line"><span>we have services that fit your needs.</span></p>
  </section>

  <section class="statement statement--support">
    <p class="statement__line"><span>Corvane can provide</span></p>
    <p class="statement__line"><span>all the front and back office support</span></p>
    <p class="statement__line"><span>your business needs to</span></p>
    <p class="statement__line"><span>thrive in Nigeria.</span></p>
  </section>

</main>
</body>
</html>
```